Label for packages of Pure Raw Natural Honeycomb

This is a label that will be used to sell pure raw honeycomb on the internet and in farm gate sales
Label must contain my Logo (which is attached)
my website www.hivelanterngold.ca
the weight 300 gr and the words Pure Raw Honeycomb
label design should fit onto a sticker 3" by 2" oval but If the size appears to small to get all that info on I am willing to look at a different size or shape

Target Market(s)

internet and in person farm gate customers

Industry/Entity Type

Agriculture

Font styles to use
Other font styles liked:
• the font should compliment my logo font

Colors
ffc214

Requirements
Must have
• Label must contain my Logo (attached) my website www.hivelanterngold.ca
• the weight 300 gr and the words Pure Raw Honeycomb would like something in black and gold with a bit of an Elegant vintage feel
Nice to have
• vintage feel
• If the size appears to small to get all that info on I am willing to look at a different size or shape
Should not have
• no cartoons

```html
<!DOCTYPE html>
<html lang="en">
<head>
<meta charset="utf-8">
<title>Hive Lantern Gold – Pure Raw Honeycomb Label</title>
<link rel="stylesheet" href="https://fonts.googleapis.com/css2?family=Pinyon+Script&family=Arimo:wght@700&display=swap">
<style>
  :root {
    --paper: #ffffff;
    --ink: #000000;
    --label-black: #050505;
    --comb-dark: #17130a;
    --gold: #d9b86a;
    --gold-deep: #b8923a;
    --ribbon-light: #fff3a6;
    --ribbon-mid: #e6c237;
    --ribbon-dark: #a9861a;
  }
  html, body {
    margin: 0;
    padding: 0;
    width: 1200px;
    height: 1200px;
    overflow: hidden;
    background: var(--paper);
  }
  .canvas {
    position: relative;
    width: 1200px;
    height: 1200px;
    box-sizing: border-box;
    border: 1px solid var(--ink);
    background: var(--paper);
  }
  .label { position: absolute; inset: 0; }
  .brand-name {
    font-family: "Pinyon Script", cursive;
    font-size: 36px;
    fill: var(--gold);
  }
  .ribbon-text {
    font-family: "Pinyon Script", cursive;
    font-size: 58px;
    fill: var(--ink);
  }
  .weight-text {
    font-family: "Arimo", Arial, sans-serif;
    font-weight: 700;
    font-size: 30px;
    fill: var(--ink);
  }
  .website-text {
    font-family: "Arimo", Arial, sans-serif;
    font-weight: 700;
    font-size: 16px;
    letter-spacing: 1px;
    fill: var(--gold);
  }
</style>
</head>
<body>
<div class="canvas">
  <svg class="label" viewBox="0 0 1200 1200" width="1200" height="1200" xmlns="http://www.w3.org/2000/svg">
    <defs>
      <linearGradient id="ribbon-gold" x1="0" y1="0" x2="0" y2="1">
        <stop offset="0" stop-color="var(--ribbon-light)"/>
        <stop offset="0.45" stop-color="var(--ribbon-mid)"/>
        <stop offset="1" stop-color="var(--ribbon-dark)"/>
      </linearGradient>
      <linearGradient id="ribbon-tail" x1="0" y1="0" x2="1" y2="1">
        <stop offset="0" stop-color="var(--ribbon-mid)"/>
        <stop offset="1" stop-color="var(--ribbon-dark)"/>
      </linearGradient>
    </defs>

    <g class="label-body">
      <ellipse cx="582" cy="568" rx="407" ry="286" fill="var(--label-black)"/>
      <ellipse cx="582" cy="568" rx="385" ry="265" fill="none" stroke="var(--gold)" stroke-width="5"/>
      <ellipse class="comb-field" role="img" aria-label="Gold honeycomb pattern on black"
               cx="582" cy="568" rx="372" ry="252" fill="var(--comb-dark)" stroke="var(--gold)" stroke-width="2"/>
    </g>

    <g class="ornaments" fill="var(--gold-deep)" opacity="0.55">
      <ellipse role="img" aria-label="Gold baroque flourish, left" cx="370" cy="445" rx="55" ry="50"/>
      <ellipse role="img" aria-label="Gold baroque flourish, right" cx="800" cy="445" rx="55" ry="50"/>
      <ellipse role="img" aria-label="Gold flourish, lower left" cx="495" cy="740" rx="50" ry="26"/>
      <ellipse role="img" aria-label="Gold flourish, lower right" cx="675" cy="740" rx="50" ry="26"/>
    </g>

    <g class="logo-medallion">
      <circle cx="588" cy="458" r="172" fill="var(--gold)"/>
      <circle cx="588" cy="458" r="167" fill="var(--label-black)"/>
      <circle cx="588" cy="420" r="34" fill="none" stroke="var(--gold)" stroke-width="4"/>
      <text class="brand-name" x="588" y="508" text-anchor="middle">Hive Lantern Gold</text>
    </g>

    <g class="ribbon">
      <polygon points="187,595 378,560 385,575 262,650 265,620" fill="url(#ribbon-tail)"/>
      <polygon points="981,595 790,560 783,575 906,650 903,620" fill="url(#ribbon-tail)"/>
      <path d="M290,585 Q580,555 880,540 L862,650 Q575,672 262,685 Z" fill="url(#ribbon-gold)"/>
      <text class="ribbon-text" x="575" y="638" text-anchor="middle" transform="rotate(-3 575 638)">Pure Raw Honeycomb</text>
    </g>

    <g class="weight-badge">
      <ellipse cx="584" cy="745" rx="69" ry="34" fill="var(--gold)" stroke="var(--label-black)" stroke-width="3"/>
      <text class="weight-text" x="584" y="756" text-anchor="middle">300 gr</text>
    </g>

    <text class="website-text" x="584" y="800" text-anchor="middle">www.hivelanterngold.ca</text>
  </svg>
</div>
</body>
</html>
```